This will turn into a huge project with mass exposure.

Tallow Crest creates soap, perfumes, rubs, lotion, etc for some of the most know brands in the market: Marisol Veil, Fern & Pebble Supply, PGR sports teams, etc.

They are going to be redesigning all logos, labels, websites and print.

They are starting with a business card and logo.

ALL designs must include a logo for Tallow Crest Holdings
Updates

Target Market(s)

Purchasers such as Marisl Veil

Industry/Entity Type

Business

Requirements
Must have
• a space for Qr code

two sided

Info:
Gavin Torlek, President
info@tallowcrest.example
555-014-2783
Nice to have
• Colors: gray background with blue and green tones. A globe that looks like an ancient map.

```html
<!DOCTYPE html>
<html lang="en">
<head>
<meta charset="utf-8">
<title>Tallow Crest Holdings — Stationery</title>
<link rel="stylesheet" href="https://fonts.googleapis.com/css2?family=Open+Sans:wght@400;600&display=swap">
<style>
  :root {
    --navy: #1a3a8c;
    --blue: #1e5fb8;
    --sky: #0a8ad8;
    --deep: #3a5596;
    --ink: #1f3f9a;
    --gray-dark: #b9b9b9;
    --gray-mid: #d6d6d6;
    --gray-light: #f4f4f4;
    --white: #ffffff;
    --text: #333333;
  }
  * { box-sizing: border-box; margin: 0; padding: 0; }
  html, body { width: 1197px; height: 1200px; overflow: hidden; background: var(--white); }
  body { font-family: "Open Sans", Arial, sans-serif; color: var(--text); }
  .sheet { position: relative; width: 1197px; height: 1200px; }

  .letterhead-page {
    position: absolute; left: 211px; top: 0; width: 926px; height: 1200px;
    background: linear-gradient(180deg, #c4c4c4 0%, #e8e8e8 25%, #f7f7f7 45%, var(--white) 65%);
  }
  .letterhead-bar {
    position: absolute; left: 211px; top: 1172px; width: 926px; height: 28px;
    background: linear-gradient(180deg, var(--navy) 0%, var(--sky) 100%);
  }

  .disc {
    position: absolute; left: 0; top: 31px; width: 294px; height: 294px; border-radius: 50%;
    background: radial-gradient(circle at 50% 50%, var(--white) 0%, var(--gray-light) 55%, var(--gray-mid) 100%);
  }
  .disc-mark {
    position: absolute; left: 92px; top: 100px; width: 200px; height: 200px; border-radius: 50%;
    background: radial-gradient(circle at 40% 40%, var(--sky) 0%, var(--blue) 60%, var(--navy) 100%);
  }
  .disc-hole {
    position: absolute; left: 110px; top: 137px; width: 82px; height: 82px; border-radius: 50%;
    background: var(--white);
  }

  .card-back {
    position: absolute; left: 165px; top: 21px; width: 322px; height: 321px;
    background: linear-gradient(180deg, var(--navy) 0%, var(--sky) 100%);
  }
  .qr-space {
    position: absolute; right: 24px; top: 60px; width: 62px; height: 62px;
    background: var(--white);
  }

  .logo { position: absolute; display: flex; flex-direction: column; align-items: center; color: var(--ink); font-weight: 600; }
  .logo-mark { border-radius: 50%; background: var(--blue); margin-bottom: 8px; }
  .logo-name { line-height: 1; white-space: nowrap; }
  .logo-sub { letter-spacing: 2px; line-height: 1.3; }
  .logo.on-blue { color: var(--white); }
  .logo.on-blue .logo-mark { background: var(--white); }

  .envelope { position: absolute; left: 558px; top: 52px; width: 625px; height: 353px; }
  .envelope-flap {
    position: absolute; left: 0; top: 0; width: 625px; height: 69px;
    background: linear-gradient(180deg, var(--navy) 0%, var(--sky) 100%);
    clip-path: polygon(1% 0, 99% 0, 100% 100%, 0 100%);
  }
  .envelope-body {
    position: absolute; left: 0; top: 69px; width: 625px; height: 284px;
    border: 1px solid #8a8a8a;
    background: radial-gradient(ellipse at 50% 35%, var(--white) 0%, #e0e0e0 45%, var(--gray-dark) 100%);
  }
  .contact { font-size: 10px; line-height: 15px; white-space: nowrap; }
  .envelope .contact { position: absolute; left: 18px; top: 232px; color: var(--text); }

  .card-gray {
    position: absolute; left: 28px; top: 391px; width: 382px; height: 217px;
    background: radial-gradient(ellipse at 50% 50%, var(--white) 0%, #e6e6e6 55%, var(--gray-dark) 100%);
  }
  .card-front {
    position: absolute; left: 297px; top: 652px; width: 383px; height: 219px;
    border: 1px solid #2a3d6d;
    background: linear-gradient(180deg, var(--deep) 0%, var(--blue) 55%, var(--sky) 100%);
    color: var(--white);
  }
  .person { position: absolute; right: 228px; top: 135px; text-align: right; white-space: nowrap; }
  .person-name { font-size: 17px; line-height: 22px; }
  .person-role { font-size: 10px; line-height: 14px; }
  .person-phone { font-size: 13px; line-height: 17px; }
  .person-email { font-size: 8.5px; line-height: 15px; }

  .card-back .contact-block { position: absolute; right: 24px; top: 278px; text-align: right; color: var(--white); white-space: nowrap; }
  .card-back .contact-block .phone { font-size: 10px; line-height: 14px; }
  .card-back .contact-block .email { font-size: 7.5px; line-height: 12px; }

  .letterhead-contact { position: absolute; left: 474px; width: 400px; top: 1120px; text-align: center; font-size: 15px; line-height: 20px; color: var(--text); }
</style>
</head>
<body>
<main class="sheet">
  <div class="letterhead-page"></div>
  <div class="letterhead-bar"></div>

  <section class="card-back" aria-label="Business card back">
    <div class="qr-space" role="img" aria-label="Space for QR code"></div>
    <div class="logo on-blue" style="left:102px; top:175px; width:200px;">
      <span class="logo-mark" style="width:44px; height:44px;"></span>
      <span class="logo-name" style="font-size:22px;">Tallow Crest</span>
      <span class="logo-sub" style="font-size:7px;">HOLDINGS</span>
    </div>
    <div class="contact-block">
      <p class="phone">555-014-2783</p>
      <p class="email">Email: info@tallowcrest.example</p>
    </div>
  </section>

  <div class="disc"></div>
  <div class="disc-mark" role="img" aria-label="Large brand mark decoration"></div>
  <div class="disc-hole"></div>

  <section class="envelope" aria-label="Envelope">
    <div class="envelope-flap"></div>
    <div class="envelope-body">
      <div class="logo" style="left:410px; top:145px; width:210px;">
        <span class="logo-mark" style="width:46px; height:46px;"></span>
        <span class="logo-name" style="font-size:22px;">Tallow Crest</span>
        <span class="logo-sub" style="font-size:7px;">HOLDINGS</span>
      </div>
      <p class="contact">Ph: 555-014-2783<br>Email: info@tallowcrest.example</p>
    </div>
  </section>

  <section class="card-gray" aria-label="Business card front, logo side">
    <div class="logo" style="left:71px; top:50px; width:240px;">
      <span class="logo-mark" style="width:60px; height:60px;"></span>
      <span class="logo-name" style="font-size:28px;">Tallow Crest</span>
      <span class="logo-sub" style="font-size:8px;">HOLDINGS</span>
    </div>
  </section>

  <div class="logo" style="left:4px; top:694px; width:200px;">
    <span class="logo-mark" style="width:62px; height:62px;"></span>
    <span class="logo-name" style="font-size:28px;">Tallow Crest</span>
    <span class="logo-sub" style="font-size:8px;">HOLDINGS</span>
  </div>

  <section class="card-front" aria-label="Business card with contact details">
    <div class="person">
      <p class="person-name">Gavin Torlek</p>
      <p class="person-role">President</p>
      <p class="person-phone">555-014-2783</p>
      <p class="person-email">Email: info@tallowcrest.example</p>
    </div>
    <div class="logo on-blue" style="left:196px; top:116px; width:180px;">
      <span class="logo-mark" style="width:46px; height:46px;"></span>
      <span class="logo-name" style="font-size:22px;">Tallow Crest</span>
      <span class="logo-sub" style="font-size:7px;">HOLDINGS</span>
    </div>
  </section>

  <div class="logo" style="left:553px; top:987px; width:240px;">
    <span class="logo-mark" style="width:62px; height:62px;"></span>
    <span class="logo-name" style="font-size:30px;">Tallow Crest</span>
    <span class="logo-sub" style="font-size:8px;">HOLDINGS</span>
  </div>
  <div class="letterhead-contact">
    <p>Ph: 555-014-2783</p>
    <p>Email: info@tallowcrest.example</p>
  </div>
</main>
</body>
</html>
```